Modern Website Design for an Online Travel Agency.. Design Only!!

Hi there!

We are building an website for our travel agency that caters to tourists traveling to the Cayman Islands. We provide travel information and take bookings for various tours available here.

We need designs for 8 different web page layouts. You can see the layout specifications in two attached documents. We do not have a need for the coding to be done. This will simply act as a blueprint for our developer to build from.

The important pages are the 'Home Page' 'checkout page' and the ‘Checkout Page’ (Page 1 & 10 in the PDF ‘Website Layout’)

The MOST important page is ‘Tour Search Page’ (page 6)

If you intend on only submitting one page design, please submit a design for page 6. Be aware though, the more of these 3 page designs you submit, the more likely we are to move forward with you!

At this stage, we are simply looking to develop the most aesthetic website design layout possible.

- The website should be colour coordinated with the logo. You can most certainly use other colours if you feel they complement the overall design of the website well.

- Everything must be laid out in an EXTREMELY simple & ‘easy to navigate’ way. The key is simplicity & Functionality. There is no need for messy or elaborate graphics.

- The website MUST have a VERY clean and modern appearance.

- We want the main background to be white, but you can use light grey in places to compliment or add dimension if you feel necessary.

- We will appreciate a good use of shadows and especially a good use of icons. (You can see examples of icons we have already designed, we are definitely open to new icon design concepts too)

- We will reward imagination and original thinking! Essentially we want a website with a creative touch and unique design elements, whilst maintaining that clean and simple layout.

- Most importantly!! - Paying attention to the small details will be highly rewarded (A well balanced and seamless use of fonts, colours, dimensions, shadowing, positioning, etc)

If you have any questions, please don’t hesitate to ask.

We’re excited to see your design submissions!

Thank you!!

You can find all the support documents and content at: https://www.filvanta.net/sh/8qm3tzprwevan47/BBQWmTfPnRxLoXEwuuiYcPvQb?dl=0

Target Market(s)

Tourists

Industry/Entity Type

Travel

Number of Pages Required

5+ page

Font styles to use
Sans Serif

Colors

Designer to choose colors to be used in the design.

Requirements
Must have
• Must be very clean and modern.
• Must be simple and bold
• Must be color coordinated in a way that makes sense
• White background
Nice to have
• Good use of shadows and Icons
Should not have
• Over use of messy graphics
• And design layout which is not right angled (using anything but vertical or horizontal for the edges in the design)

```html
<!DOCTYPE html>
<html lang="en">
<head>
<meta charset="utf-8">
<title>Coral Lagoon – Cayman Islands | IsleRoute</title>
<link href="https://fonts.googleapis.com/css2?family=Roboto:ital,wght@0,400;0,500;0,700;0,900;1,400&display=swap" rel="stylesheet">
<style>
:root{
  --green:#7ab830;
  --green-dark:#5f9a1f;
  --blue:#1766d6;
  --blue-dark:#0e4fb0;
  --ink:#1d1f24;
  --text:#3b3f46;
  --muted:#8a8f98;
  --line:#e4e7ec;
  --panel:#f1f3f5;
  --white:#ffffff;
  --sea-1:#0d5fb8;
  --sea-2:#1c8fd0;
  --sea-3:#2fb3c9;
  --footer:#1d2024;
}
*{box-sizing:border-box;margin:0;padding:0}
html,body{width:1200px;height:5381px;overflow:hidden}
body{font-family:"Roboto",Arial,sans-serif;color:var(--text);background:var(--white);position:relative;font-size:14px}
.abs{position:absolute}
a{color:inherit;text-decoration:none}

/* header + hero */
.hero{top:0;left:0;width:1200px;height:627px;background:linear-gradient(160deg,#0e6a63 0%,#1a8a7d 35%,#2a6d8f 70%,#12385c 100%)}
.topbar{top:24px;left:77px;width:1046px;height:46px;display:flex;align-items:center;color:#fff}
.brand{display:flex;align-items:center;gap:8px;font-weight:700;font-size:26px;color:var(--green);margin-right:34px}
.brand i{width:30px;height:30px;border-radius:4px;background:var(--green);display:block}
.nav{display:flex;gap:22px;font-size:14px}
.top-right{margin-left:auto;display:flex;align-items:center;gap:18px;font-size:14px;color:#f3c53a;font-weight:500}
.dest{border:1px solid #fff;border-radius:4px;color:#fff;padding:12px 16px;font-weight:700}
.hero h1{top:236px;left:0;width:1200px;text-align:center;color:#fff;font-weight:900;font-size:74px;line-height:1}
.hero h2{top:322px;left:0;width:1200px;text-align:center;color:#fff;font-weight:900;font-size:50px;line-height:1}
.loc-tag{top:574px;left:77px;width:218px;height:53px;background:var(--green);color:#fff;display:flex;align-items:center;gap:10px;padding-left:26px;font-size:19px;border-radius:4px 4px 0 0}
.see-photos{top:477px;left:800px;width:174px;height:46px;background:var(--green);color:#fff;border-radius:4px;display:flex;align-items:center;justify-content:center;gap:8px;font-size:18px}

/* sidebar */
.price{top:537px;left:800px;width:322px;height:86px;background:var(--green);color:#fff;padding:16px 26px;border-radius:4px 4px 0 0}
.price small{font-size:14px;display:block}
.price b{font-size:36px;font-weight:700}
.price span{font-size:15px}
.book-card{top:623px;left:800px;width:322px;height:340px;border:1px solid var(--line);border-top:none;text-align:center;padding-top:40px;box-shadow:0 6px 18px rgba(0,0,0,.05)}
.stars{color:#f4b400;font-size:24px;letter-spacing:2px}
.reviews{color:var(--muted);text-decoration:underline;font-size:14px;margin-top:4px}
.btn{display:inline-flex;align-items:center;justify-content:center;border-radius:4px;font-weight:500;text-transform:uppercase;font-size:16px}
.btn-blue{background:var(--blue);color:#fff}
.btn-green{background:var(--green);color:#fff}
.book-card .btn-blue{width:270px;height:54px;margin-top:30px;font-size:18px}
.gift{width:270px;height:50px;margin:8px auto 0;border:2px solid var(--blue);border-radius:4px;color:var(--blue);display:flex;align-items:center;justify-content:center;gap:8px;font-size:15px}
.popular{margin-top:30px;font-weight:700;color:var(--ink);font-size:14px}
.popular-sub{font-size:13px;color:var(--muted);margin-top:6px}
.need-help{top:982px;left:800px;width:322px;text-align:center;color:var(--muted);font-size:14px;font-weight:500}
.help-btn{top:1030px;height:50px;width:155px;border:1px solid var(--line);background:#f6f7f8;border-radius:4px;display:flex;align-items:center;justify-content:center;gap:10px;font-size:16px}

/* breadcrumb + tabs */
.crumbs{top:645px;left:77px;font-size:13px;color:var(--muted);display:flex;gap:12px}
.tabs{top:700px;left:77px;width:698px;display:flex;gap:46px;font-size:15px;border-bottom:1px solid var(--line);height:34px}
.tabs span::before{content:"";display:inline-block;width:6px;height:6px;border-radius:50%;background:var(--green);margin-right:8px;vertical-align:middle}
.tabs .on{font-weight:700;color:var(--ink);border-bottom:3px solid var(--green);padding:0 8px}

.box{left:77px;width:698px;border:1px solid var(--line);background:#fff}
.box h3{font-size:17px;font-weight:700;color:var(--ink);text-transform:uppercase}
.desc-box{top:752px;height:372px;background:var(--panel);padding:30px 28px 0}
.feat-grid{display:grid;grid-template-columns:1fr 1fr;row-gap:40px;margin-top:34px}
.feat{display:flex;gap:14px}
.feat b{display:block;font-size:17px;color:var(--ink);font-weight:500}
.feat p{font-size:13px;color:var(--muted);margin-top:8px}
.feat .letters{color:var(--green);letter-spacing:6px;font-weight:700;font-size:13px}
.organizer{position:absolute;left:0;bottom:0;width:100%;height:80px;background:#e6e8eb;display:flex;align-items:center;justify-content:center;gap:14px;font-size:14px;color:var(--ink)}
.organizer i{width:62px;height:62px;border-radius:50%;background:#3a2d28;display:block}
.organizer a{text-decoration:underline}

.text-box{top:1156px;height:418px;padding:30px 28px;overflow:hidden}
.text-box .lead{font-style:italic;font-size:15px;line-height:29px;margin-top:22px;color:var(--ink)}
.text-box .strong{font-weight:500;color:var(--ink);margin-top:26px;font-size:15px}
.text-box .fade{color:#c9ccd1;margin-top:26px;font-size:14px;line-height:26px}
.more{position:absolute;left:0;bottom:0;width:100%;height:104px;background:var(--panel);text-align:center;padding-top:32px;font-size:15px;color:var(--ink)}
.more small{display:block;font-size:14px;color:var(--text);margin-top:10px}
.more i{position:absolute;right:20px;top:34px;width:40px;height:40px;border-radius:50%;background:var(--green)}

/* tour section */
.tour-sec{top:1634px;left:0;width:1200px;height:1585px;background:linear-gradient(180deg,var(--sea-1) 0%,var(--sea-2) 35%,var(--sea-3) 70%,#2aa0c6 100%)}
.tour-sec h2{position:absolute;top:60px;width:100%;text-align:center;color:#fff;font-size:40px;font-weight:500}
.tour-card{left:77px;width:1045px;background:#fff;border-radius:3px}
.tour-head{height:100px;display:flex;align-items:center;padding:0 18px 0 36px;border-bottom:1px solid var(--line)}
.tour-head h3{font-size:30px;color:var(--green);font-weight:500}
.tour-head .amt{margin-left:auto;font-size:24px;color:var(--green);font-weight:500;margin-right:28px}
.tour-head .btn{height:46px;font-size:15px}
.tour-body{position:absolute;top:100px;left:14px;width:1017px;height:1010px;display:flex;background:linear-gradient(180deg,#b9cfe0 0%,#9fc2c9 50%,#6fb9c7 100%)}
.tour-left{width:397px;background:rgba(230,240,250,.85);padding:40px 24px}
.tour-right{flex:1;padding:46px 44px;color:#1e2a36;background:rgba(190,210,225,.55)}
.fact{display:flex;gap:14px;margin-bottom:36px}
.fact b{font-size:16px;color:var(--ink);font-weight:500}
.fact ul{list-style:none;margin-top:8px;font-size:13px;color:var(--text)}
.fact li{margin-top:13px}
.fact li::before{content:"•";margin-right:10px}
.fact.green b{color:var(--green-dark)}
.fact.green li{color:var(--green-dark)}
.fact.red b{color:#e53935}
.fact.red li{color:#e53935}
.fact.blue b{color:var(--blue)}
.fact.blue li{color:var(--blue)}
.ico{width:26px;height:26px;flex:none}
.tour-right h4{font-size:22px;font-weight:500;color:var(--ink)}
.tour-right p{font-size:13.5px;line-height:27px;margin-top:16px}
.tour-right .gap{margin-top:72px}
.hide{position:absolute;bottom:0;width:100%;height:50px;border-top:1px solid var(--line);display:flex;align-items:center;justify-content:center;color:var(--muted);font-size:14px;gap:8px}

/* meeting point */
.meet{top:3273px;left:77px;width:1045px;height:479px;border:1px solid var(--line);box-shadow:0 4px 16px rgba(0,0,0,.06)}
.meet h3{position:absolute;top:36px;left:34px;font-size:30px;font-weight:700;color:var(--ink)}
.meet p{position:absolute;top:106px;left:34px;width:280px;font-size:14px;line-height:28px}
.meet .btn{position:absolute;top:190px;left:34px;width:178px;height:48px;font-size:15px}
.map{position:absolute;top:18px;left:365px;width:662px;height:444px;background:linear-gradient(135deg,#dfe9ee,#cfe1d9 60%,#dfe9ee)}

.gallery-title{top:3805px;left:0;width:1200px;text-align:center;font-size:40px;font-weight:500;color:var(--ink)}
.photo{width:334px;height:245px}

/* promo */
.promo{top:4456px;left:77px;width:1045px;height:529px;background:#e6f1fb}
.step{position:absolute;top:80px;left:28px;width:86px;height:86px;border-radius:50%;background:#fff;color:var(--blue);font-size:38px;display:flex;align-items:center;justify-content:center}
.promo h3{position:absolute;top:196px;left:28px;font-size:34px;font-weight:400;color:var(--blue);line-height:40px}
.promo p{position:absolute;top:300px;left:28px;width:360px;font-size:14px;line-height:28px;color:var(--ink)}
.promo .b1{position:absolute;top:381px;left:28px;width:214px;height:48px;font-size:15px}
.promo .b2{position:absolute;top:381px;left:256px;width:224px;height:48px;font-size:15px}
.illus{position:absolute;top:50px;left:540px;width:470px;height:420px;background:radial-gradient(circle at 50% 55%,#c9dff4 0%,#e6f1fb 70%)}
.dots{position:absolute;bottom:20px;left:0;width:100%;display:flex;justify-content:center;gap:6px}
.dots i{width:12px;height:12px;border-radius:50%;border:2px solid var(--blue);display:block}
.dots i.on{background:var(--blue)}

/* footer */
.footer{top:5052px;left:0;width:1200px;height:329px;background:linear-gradient(180deg,#24282d,var(--footer))}
.footer .brand{position:absolute;top:160px;left:96px;font-size:30px}
.socials{position:absolute;top:222px;left:118px;display:flex;gap:12px}
.socials i{width:40px;height:40px;border-radius:50%;background:var(--blue);display:block}
.fcol{position:absolute;top:44px;font-size:14px;color:#9aa0a8}
.fcol h5{color:var(--green);font-size:16px;font-weight:500;margin-bottom:20px}
.fcol li{list-style:none;margin-bottom:15px}
.nl-input{width:282px;height:46px;background:#fff;margin-top:16px;color:#777;padding:14px 16px;font-size:13px}
.nl-btn{width:138px;height:44px;margin-top:10px;font-size:15px}
.copy{position:absolute;bottom:0;left:250px;width:700px;height:56px;border-top:1px solid #3a3e44;display:flex;align-items:center;justify-content:center;color:#888d95;font-size:14px}
.copy b{color:var(--green);font-weight:400}
</style>
</head>
<body>

<section class="hero abs" role="img" aria-label="Photo of a smiling girl with a dolphin in clear water">
  <header class="topbar abs">
    <div class="brand"><i></i>IsleRoute</div>
    <nav class="nav"><a>Discover Cayman</a><a>Thing To Do</a><a>My Trip Planner</a><a>Map</a><a>Contact Us</a></nav>
    <div class="top-right"><span>USD$</span><span>LOGIN</span><span class="dest">Destinations ⌄</span></div>
  </header>
  <h1 class="abs">CORAL LAGOON</h1>
  <h2 class="abs">CAYMAN ISLANDS</h2>
  <div class="loc-tag abs">
    <svg width="16" height="20" viewBox="0 0 16 20"><path d="M8 1a6 6 0 0 0-6 6c0 5 6 12 6 12s6-7 6-12a6 6 0 0 0-6-6z" fill="none" stroke="#fff" stroke-width="2"/><circle cx="8" cy="7" r="2" fill="#fff"/></svg>
    Cayman Islands
  </div>
  <div class="see-photos abs">
    <svg width="20" height="16" viewBox="0 0 20 16"><rect x="1" y="2" width="18" height="13" rx="2" fill="none" stroke="#fff" stroke-width="2"/><path d="M4 12l4-4 3 3 2-2 3 3" fill="none" stroke="#fff" stroke-width="1.5"/></svg>
    See Photos
  </div>
</section>

<aside>
  <div class="price abs"><small>From</small><b>$230.0</b><span> / person</span></div>
  <div class="book-card abs">
    <div class="stars">★★★★★</div>
    <div class="reviews">22 Reviews</div>
    <a class="btn btn-blue">Book now</a>
    <div class="gift">
      <svg width="18" height="18" viewBox="0 0 18 18"><rect x="2" y="7" width="14" height="10" fill="#7ab830"/><rect x="1" y="4" width="16" height="4" fill="#1766d6"/><rect x="8" y="4" width="2" height="13" fill="#fff"/></svg>
      Gift
    </div>
    <div class="popular">This offer is very popular</div>
    <div class="popular-sub">1133 people recently chose this activity</div>
  </div>
  <div class="need-help abs">Need Help?</div>
  <div class="help-btn abs" style="left:800px">
    <svg width="22" height="22" viewBox="0 0 22 22"><rect x="4" y="2" width="12" height="18" rx="2" fill="none" stroke="#1766d6" stroke-width="2"/><circle cx="17" cy="15" r="4" fill="#7ab830"/></svg>
    Call Us
  </div>
  <div class="help-btn abs" style="left:966px">
    <svg width="24" height="20" viewBox="0 0 24 20"><rect x="1" y="2" width="16" height="11" rx="2" fill="#7ab830"/><rect x="8" y="7" width="14" height="10" rx="2" fill="#1766d6"/></svg>
    Email Us
  </div>
</aside>

<div class="crumbs abs"><span>Homepage</span>›<span>Tour</span>›<span>Cayman Islands</span>›<span>Coral Lagoon</span></div>
<div class="tabs abs"><span class="on">Activity Discription</span><span>Tour</span><span>Meeting Point</span><span>Photo Gallery</span></div>

<section class="box desc-box abs">
  <h3>Activity Description</h3>
  <div class="feat-grid">
    <div class="feat">
      <svg class="ico" viewBox="0 0 26 26"><path d="M4 4h18l-9 10z" fill="#f4b400"/><rect x="12" y="12" width="2" height="12" fill="#1766d6"/></svg>
      <div><b>Tour Description</b><p>Lorem Ipsum is the simply text.</p></div>
    </div>
    <div class="feat">
      <svg class="ico" viewBox="0 0 26 26"><rect x="1" y="3" width="16" height="11" rx="2" fill="#1766d6"/><rect x="9" y="10" width="16" height="11" rx="2" fill="#7ab830"/></svg>
      <div><b>Spoken Languages</b><p>Lorem Ipsum is the simply text.</p></div>
    </div>
    <div class="feat">
      <svg class="ico" viewBox="0 0 26 26"><path d="M3 23l8-18 8 18z" fill="#1766d6"/><path d="M13 23l6-12 5 12z" fill="#7ab830"/></svg>
      <div><b>Open Seasons</b><p class="letters">KMHVGACROD</p></div>
    </div>
    <div class="feat">
      <svg class="ico" viewBox="0 0 26 26"><path d="M3 14l7 7L24 4" fill="none" stroke="#1766d6" stroke-width="3"/></svg>
      <div><b>Cancellation Policy</b><p>Lorem Ipsum text.</p></div>
    </div>
  </div>
  <div class="organizer"><i role="img" aria-label="Organizer badge"></i>Organized by <a>Harborline Tours</a></div>
</section>

<section class="box text-box abs">
  <h3>Activity Description</h3>
  <p class="lead">Lorem Ipsum is simply dummy text of the printing and typesetting industry. Lorem Ipsum has been the industry's standard dummy text ever since the 1500s, when an unknown printer took a galley of type and scrambled it to make a type specimen book. It has survived not only five centuries, but also the leap.</p>
  <p class="strong">Lorem Ipsum is simply dummy printing &amp; type.</p>
  <p class="fade">Lorem Ipsum is simply dummy text of the printing and typesetting industry. Lorem Ipsum has been the industry's standard dummy text ever since the 1500s, when an unknown.</p>
  <div class="more">MORE INFORMATION<small>Requirements, special terms &amp; more</small>
    <i><svg width="40" height="40" viewBox="0 0 40 40"><path d="M12 20h15M21 14l6 6-6 6" fill="none" stroke="#fff" stroke-width="3"/></svg></i>
  </div>
</section>

<section class="tour-sec abs" aria-label="Tour">
  <h2>Tour</h2>
  <article class="tour-card abs" style="top:143px;height:1208px">
    <div class="tour-head">
      <h3>TOUR 1</h3>
      <span class="amt">$230.0</span>
      <a class="btn btn-blue" style="width:146px">Book now</a>
      <a class="btn btn-green" style="width:190px;margin-left:12px">Add to itinerary</a>
    </div>
    <div class="tour-body" role="img" aria-label="Background photo of a sandy beach and turquoise sea">
      <div class="tour-left">
        <div class="fact"><svg class="ico" viewBox="0 0 26 26"><circle cx="13" cy="14" r="10" fill="none" stroke="#1766d6" stroke-width="2.5"/><path d="M13 8v6h5" fill="none" stroke="#f4b400" stroke-width="2.5"/></svg>
          <div><b>Duration</b><ul><li>4 hrs</li></ul></div></div>
        <div class="fact"><svg class="ico" viewBox="0 0 26 26"><circle cx="13" cy="5" r="3" fill="#1766d6"/><rect x="10" y="9" width="6" height="15" rx="2" fill="#1766d6"/></svg>
          <div><b>Minimum Age</b><ul><li>Minimum 12y / o</li></ul></div></div>
        <div class="fact"><svg class="ico" viewBox="0 0 26 26"><path d="M13 2v22M2 13h22" stroke="#1766d6" stroke-width="3"/><circle cx="13" cy="13" r="4" fill="#7ab830"/></svg>
          <div><b>Starting Times</b><ul><li>Starting time to be define with your pro.</li></ul></div></div>
        <div class="fact"><svg class="ico" viewBox="0 0 26 26"><circle cx="13" cy="8" r="5" fill="none" stroke="#1766d6" stroke-width="2.5"/><path d="M3 24c2-7 18-7 20 0" fill="none" stroke="#7ab830" stroke-width="2.5"/></svg>
          <div><b style="text-decoration:underline">Metting Point</b></div></div>
        <div class="fact green"><svg class="ico" viewBox="0 0 26 26"><circle cx="13" cy="13" r="11" fill="#7ab830"/><path d="M8 13l4 4 7-8" fill="none" stroke="#fff" stroke-width="2.5"/></svg>
          <div><b>Included</b><ul><li>Buffet breakfast at launch site</li><li>Light lunch</li><li>Snacks</li><li>Refreshments</li><li>Afternoon tea</li><li>Certificate of attendance</li></ul></div></div>
        <div class="fact red"><svg class="ico" viewBox="0 0 26 26"><circle cx="13" cy="13" r="11" fill="#e53935"/><path d="M9 9l8 8M17 9l-8 8" stroke="#fff" stroke-width="2.5"/></svg>
          <div><b>Excluded</b><ul><li>Video (350Rand)</li></ul></div></div>
        <div class="fact blue"><svg class="ico" viewBox="0 0 26 26"><path d="M13 3l11 20H2z" fill="#1766d6"/><rect x="12" y="10" width="2" height="7" fill="#fff"/></svg>
          <div><b>What To Bring</b><ul><li>Sunscreen</li><li>Passport or Driving licence</li><li>Swimwear</li><li>Towel</li><li>Camera</li><li>Hat or cap</li><li>A warm jacket</li></ul></div></div>
      </div>
      <div class="tour-right">
        <h4>Tour Description</h4>
        <p>Lorem Ipsum is simply dummy text of the printing and typesetting industry has been the industry's standard dummy text.</p>
        <p>Lorem Ipsum is simply dummy text of the printing and typesetting industry. Lorem Ipsum has been the industry's standard dummy text ever since the 1500s, when an unknown.</p>
        <p>Lorem Ipsum is simply dummy text of the printing and typesetting industry has been the</p>
        <p>Lorem Ipsum is simply dummy text of the printing and typesetting industry. been the industry's standard dummy.</p>
        <p>Lorem Ipsum is simply dummy text of the print.</p>
        <h4 class="gap">Activity Requirements</h4>
        <p style="margin-top:4px">Lorem Ipsum is simply dummy text of the printing and.</p>
        <h4 style="margin-top:90px">Additional Info</h4>
        <p style="font-weight:500">Lorem Ipsum is simply dummy text of the printing and typesetting industry. Lorem Ipsum has been the industry's standard dummy text ever since the 1500s, when an unknown.</p>
        <p>Lorem Ipsum is simply dummy text of the printing and typesetting industry. Lorem Ipsum has been the industry's standard dummy text.</p>
      </div>
    </div>
    <div class="hide">Hide Details ⌄</div>
  </article>

  <article class="tour-card abs" style="top:1374px;height:142px">
    <div class="tour-head" style="padding-left:28px">
      <h3>TOUR 2</h3>
      <span class="amt">$230.0</span>
      <a class="btn btn-blue" style="width:146px">Book now</a>
      <a class="btn btn-green" style="width:190px;margin-left:12px">Add to itinerary</a>
    </div>
    <div class="hide" style="height:42px">Hide Details ⌄</div>
  </article>
</section>

<section class="meet abs">
  <h3>MEETING POINT</h3>
  <p>Coral Lagoon Cayman Islands, Lorem Ipsum is simply dummy text.</p>
  <a class="btn btn-blue">Get directions</a>
  <div class="map" role="img" aria-label="Map of Grand Cayman showing the meeting point"></div>
</section>

<h2 class="gallery-title abs">PHOTO GALLERY</h2>
<div class="photo abs" style="top:3898px;left:77px;background:linear-gradient(180deg,#0c1624,#2b3b52)" role="img" aria-label="Riders on horseback silhouetted at dusk"></div>
<div class="photo abs" style="top:3898px;left:433px;background:linear-gradient(160deg,#2fb4c2,#15808e)" role="img" aria-label="Swimmer with a dolphin"></div>
<div class="photo abs" style="top:3898px;left:788px;background:linear-gradient(180deg,#5aa0d8,#2e7fb8 60%,#4aa7c9)" role="img" aria-label="Man jumping into the sea"></div>
<div class="photo abs" style="top:4165px;left:77px;background:linear-gradient(180deg,#7fb6d8,#3e8fb4 55%,#8a6a4f)" role="img" aria-label="Woman riding a horse in shallow water"></div>
<div class="photo abs" style="top:4165px;left:433px;background:linear-gradient(180deg,#3f86c8,#2a6fae 60%,#3d9ab5)" role="img" aria-label="Group of friends jumping on the beach"></div>
<div class="photo abs" style="top:4165px;left:788px;background:linear-gradient(180deg,#cfe5f0,#8fbfd6 60%,#6d4a33)" role="img" aria-label="Rider with a horse at the shore"></div>

<section class="promo abs">
  <div class="step">1</div>
  <h3>Choose Your<br>Favorite Activities</h3>
  <p>Discover everything you need to know about travel &amp; safety in the cayman Islands and browse every fun activity available here.</p>
  <a class="btn btn-blue b1">Learn about Cayman</a>
  <a class="btn btn-green b2">Finding things to do</a>
  <div class="illus" role="img" aria-label="Illustration of a traveller planning a trip at a laptop with a suitcase"></div>
  <div class="dots"><i class="on"></i><i></i><i></i><i></i></div>
</section>

<footer class="footer abs" role="contentinfo">
  <div class="brand"><i></i>IsleRoute</div>
  <div class="socials"><i aria-label="Social link"></i><i aria-label="Social link"></i><i aria-label="Social link"></i><i aria-label="Social link"></i></div>
  <div class="fcol" style="left:394px"><h5>SITEMAP</h5><ul><li>Discover Cayman</li><li>Thing To Do</li><li>My Trip planner</li><li>Map</li><li>Contact Us</li></ul></div>
  <div class="fcol" style="left:626px"><h5>SUPPORT</h5><ul><li>FAQ</li><li>Legal notices</li><li>Cancellation policy</li><li>Terms of use</li><li>Privacy policy</li></ul></div>
  <div class="fcol" style="left:844px"><h5>NEWSLETTER</h5><div>Sign up For our exclusive Update !</div>
    <div class="nl-input">Enter Email*</div>
    <a class="btn btn-blue nl-btn">Subscribe</a>
  </div>
  <div class="copy">©<b>IsleRoute</b>&nbsp;- 2019 All rights reserved.</div>
</footer>

</body>
</html>
```